Editorial Website Design for High-End Custom Millwork Firm

Design (no development) for a 5-7 page website for a high-end custom architectural millwork firm. Editorial, magazine-quality aesthetic — think Interior Almanac and top-tier millwork studios (Elwin Strade, Korvo). Full brief, reference sites, and project photography attached. We have uploaded a sample of our photography to use in your design. PLEASE READ PDF DOCUMENT BRIEF!!!

1 page

```html
<!DOCTYPE html>
<html lang="en">
<head>
<meta charset="utf-8">
<title>Halden Architectural Millwork</title>
<link href="https://fonts.googleapis.com/css2?family=Sorts+Mill+Goudy&family=Poppins:wght@400;500;600;700&display=swap" rel="stylesheet">
<style>
:root{
  --stage:#000000;
  --cream:#f7f4ee;
  --stone:#ece9e3;
  --white:#ffffff;
  --ink:#111111;
  --tan:#8f8377;
  --rule:#cfcac2;
  --muted:#8a8580;
  --charcoal:#4a4846;
  --band:#444444;
  --quote:#d6d6d6;
}
*{box-sizing:border-box;margin:0;padding:0}
html,body{width:722px;height:1200px;overflow:hidden;background:var(--stage)}
.page{position:absolute;left:0;top:0;width:607px;height:1959px;background:var(--cream);
  transform-origin:0 0;transform:translate(175.2px,0) scale(0.6125);
  font-family:"Poppins",sans-serif;color:var(--ink)}
.abs{position:absolute}
.serif{font-family:"Sorts Mill Goudy",serif;font-weight:400}
.rule-h{position:absolute;height:1px;background:var(--rule)}
.rule-v{position:absolute;width:1px;background:var(--rule)}
.btn{position:absolute;background:var(--ink);color:#fff;font-family:"Sorts Mill Goudy",serif;
  font-size:7px;display:flex;align-items:center;justify-content:center;gap:8px}
.btn svg{width:9px;height:6px}
.circle-arrow{position:absolute;width:19px;height:19px;border-radius:50%;background:#fff;display:flex;align-items:center;justify-content:center}
.circle-arrow.dark{background:#111}
.circle-arrow svg{width:9px;height:6px}
.photo{position:absolute}

/* header */
.site-header{position:absolute;left:0;top:0;width:607px;height:67px;background:var(--cream);border-bottom:1px solid var(--rule)}
.brand{position:absolute;left:282px;top:10px;width:43px;height:18px;background:#5a5550;color:#f1ece4;
  font-family:"Sorts Mill Goudy",serif;font-size:12px;display:flex;align-items:center;justify-content:center;letter-spacing:1px}
.nav{position:absolute;left:0;top:36px;width:607px;height:30px;border-top:1px solid var(--rule);display:flex;justify-content:center;gap:0}
.nav a{font-size:6px;color:var(--ink);text-decoration:none;padding:11px 11px 0;height:30px}
.nav a.active{font-weight:600;border-bottom:2px solid var(--ink);height:24px}

/* hero */
.hero{position:absolute;left:0;top:67px;width:607px;height:280px;
  background:linear-gradient(110deg,#b9ab98 0%,#d8cfc2 35%,#e6e0d6 55%,#c9b79e 80%,#a08a70 100%)}
.hero-eyebrow{left:33px;top:46px;font-size:5px;color:#fff;letter-spacing:.3px}
.hero-title{left:33px;top:70px;font-size:20px;line-height:26px;color:#fff}
.hero-copy{left:33px;top:158px;width:160px;font-size:6px;line-height:13px;color:#fff}
.hero-dots{left:0;top:249px;width:607px;height:31px;background:rgba(70,60,50,.25)}
.dot{position:absolute;top:12px;font-size:5px;color:#fff}

/* tagline */
.tagline{left:0;top:381px;width:607px;text-align:center;font-size:16px;font-weight:600;color:var(--tan)}

/* featured */
.featured{position:absolute;left:0;top:437px;width:607px;height:306px;background:var(--stone);border-top:1px solid var(--rule);border-bottom:1px solid var(--rule)}
.featured-top{position:absolute;left:0;top:0;width:607px;height:91px;background:var(--cream)}
.section-title{font-size:22px;line-height:26px}
.cat-list{position:absolute;left:33px;top:106px;list-style:none}
.cat-list li{font-size:6px;color:var(--muted);height:20px}
.cat-list li.on{color:var(--ink);font-weight:600;font-size:7px}

/* our work */
.work-title{left:0;top:790px;width:607px;text-align:center;font-size:16px;font-weight:600;color:var(--tan)}
.work-label{font-size:20px;color:#fff}
.work-copy{font-size:6px;line-height:13px}

/* news */
.news{position:absolute;left:0;top:1075px;width:607px;height:480px;background:var(--cream);border-top:1px solid var(--rule)}
.card-shade{position:absolute;left:0;bottom:0;width:100%;height:58px;background:rgba(60,60,60,.45)}
.card-eyebrow{font-size:5px;color:#fff}
.card-title{font-size:8px;color:#fff;line-height:14px}
.quote-box{position:absolute;left:309px;top:1273px;width:298px;height:112px;background:var(--quote)}

/* testimonial / cta */
.testimonial-name{font-size:22px}
.small{font-size:6px;line-height:13px}

/* footer */
.site-footer{position:absolute;left:0;top:1843px;width:607px;height:116px;background:var(--charcoal);color:#cfcac2}
.foot-brand{position:absolute;left:33px;top:23px;width:64px;height:28px;background:#5f5b57;border:1px solid #8a8580;
  font-family:"Sorts Mill Goudy",serif;font-size:18px;color:#e9e3da;display:flex;align-items:center;justify-content:center;letter-spacing:2px}
.tiny{font-size:4.5px;line-height:8px;color:#b8b2aa}
.social{position:absolute;width:11px;height:11px;border-radius:50%;border:1px solid #cfcac2}
</style>
</head>
<body>
<div class="page">

  <header class="site-header">
    <div class="brand">Halden</div>
    <nav class="nav">
      <a class="active">Home</a><a>Service</a><a>Project</a><a>Our Story</a><a>Blog</a><a>Contact Us</a>
    </nav>
  </header>

  <section class="hero" role="img" aria-label="Bright custom kitchen with cream cabinetry, pendant lights and a fluted oak island">
    <p class="abs hero-eyebrow">CUSTOM ARCHITECTURAL MILLWORK &amp; CABINETRY</p>
    <h1 class="abs serif hero-title">Crafted for<br>Architecture<br>Build to Last.</h1>
    <p class="abs hero-copy">Award-winning custom architectural millwork and cabinetry for commercial interiors and luxury residences.</p>
    <div class="btn" style="left:33px;top:206px;width:88px;height:18px">Explore Our Work
      <svg viewBox="0 0 9 6"><path d="M0 3h8M5.5 .5 8 3 5.5 5.5" stroke="#fff" fill="none" stroke-width=".8"/></svg></div>
    <div class="abs hero-dots">
      <span class="dot" style="left:268px">01</span>
      <div class="abs" style="left:258px;top:22px;width:28px;height:1px;background:#fff"></div>
      <span class="dot" style="left:300px">02</span>
      <span class="dot" style="left:332px">03</span>
    </div>
  </section>

  <div class="abs" style="left:0;top:347px;width:607px;height:90px;background:var(--white)"></div>
  <div class="rule-v" style="left:303px;top:347px;height:26px"></div>
  <p class="abs tagline">Precision. Craftsmanship. Timeless Design.</p>
  <div class="rule-v" style="left:303px;top:410px;height:27px"></div>

  <section class="featured">
    <div class="featured-top"></div>
    <h2 class="abs serif section-title" style="left:33px;top:24px">Featured<br>Projects</h2>
    <ul class="cat-list">
      <li class="on">
        <svg width="9" height="6" viewBox="0 0 9 6" style="margin-right:5px"><path d="M0 3h8M5.5 .5 8 3 5.5 5.5" stroke="#111" fill="none" stroke-width=".8"/></svg>Commercial Millwork</li>
      <li>Residential Cabinetry</li>
      <li>Architectural Woodwork</li>
      <li>Design Collaboration</li>
      <li>Engineering &amp; Shop Drawings</li>
      <li>Custom Fabrication</li>
      <li>Installation</li>
      <li>Quality Assurance</li>
    </ul>
    <div class="photo" role="img" aria-label="Modern white kitchen with marble backsplash and warm wood cabinetry" style="left:171px;top:24px;width:402px;height:235px;background:linear-gradient(100deg,#e9e6e1 0%,#f1efeb 40%,#e4ddd2 70%,#c9ab82 100%)"></div>
    <div class="rule-h" style="left:33px;top:281px;width:433px;background:#b9b4ac"></div>
    <div class="btn" style="left:477px;top:272px;width:97px;height:18px">View All Project
      <svg viewBox="0 0 9 6"><path d="M0 3h8M5.5 .5 8 3 5.5 5.5" stroke="#fff" fill="none" stroke-width=".8"/></svg></div>
  </section>

  <div class="abs" style="left:0;top:744px;width:607px;height:331px;background:var(--white)"></div>
  <div class="rule-v" style="left:303px;top:744px;height:42px"></div>
  <h2 class="abs work-title">Our Work</h2>

  <div class="photo" role="img" aria-label="Commercial lobby with dark wood millwork and decorative ceiling lights" style="left:0;top:824px;width:302px;height:182px;background:linear-gradient(180deg,#5a4a3a 0%,#3d3128 60%,#2a231d 100%)"></div>
  <p class="abs serif work-label" style="left:33px;top:976px">Commercial</p>
  <div class="circle-arrow" style="left:276px;top:980px"><svg viewBox="0 0 9 6"><path d="M0 3h8M5.5 .5 8 3 5.5 5.5" stroke="#111" fill="none" stroke-width=".8"/></svg></div>

  <div class="photo" role="img" aria-label="Residential kitchen with walnut cabinetry and dark stone island" style="left:303px;top:824px;width:304px;height:182px;background:linear-gradient(180deg,#e8e2d8 0%,#b37544 50%,#4a3c33 100%)"></div>
  <p class="abs serif work-label" style="left:309px;top:972px">Residential</p>
  <div class="circle-arrow dark" style="left:554px;top:976px"><svg viewBox="0 0 9 6"><path d="M0 3h8M5.5 .5 8 3 5.5 5.5" stroke="#fff" fill="none" stroke-width=".8"/></svg></div>

  <p class="abs work-copy" style="left:33px;top:1019px;width:260px">Luxury hotels, universities, retail environments, corporate spaces, healthcare, and hospitality projects crafted to the highest architectural standards.</p>
  <p class="abs work-copy" style="left:309px;top:1019px;width:260px;color:var(--muted)">Custom kitchens, libraries, wine rooms, built-ins, and architectural interiors designed for exceptional homes.</p>

  <section class="news"></section>
  <h2 class="abs serif section-title" style="left:33px;top:1112px">Explore our<br>lates news</h2>
  <div class="btn" style="left:216px;top:1141px;width:82px;height:18px">See All News
    <svg viewBox="0 0 9 6"><path d="M0 3h8M5.5 .5 8 3 5.5 5.5" stroke="#fff" fill="none" stroke-width=".8"/></svg></div>

  <div class="abs" style="left:0;top:1514px;width:298px;height:39px;background:var(--band)"></div>

  <article class="photo" role="img" aria-label="Craftsman assembling a lattice millwork panel in the shop" style="left:33px;top:1174px;width:265px;height:160px;background:linear-gradient(160deg,#a89b88,#6f6555)">
    <div class="card-shade"></div>
    <p class="abs card-eyebrow" style="left:16px;top:112px">COMMERCIAL</p>
    <p class="abs serif card-title" style="left:16px;top:125px;width:200px">Crafting Bespoke Millwork for Extraordinary Spaces</p>
    <div class="circle-arrow" style="left:234px;top:120px"><svg viewBox="0 0 9 6"><path d="M0 3h8M5.5 .5 8 3 5.5 5.5" stroke="#111" fill="none" stroke-width=".8"/></svg></div>
  </article>

  <article class="photo" role="img" aria-label="Craftsman shaping a curved wooden frame in the workshop" style="left:33px;top:1344px;width:265px;height:160px;background:linear-gradient(160deg,#8c7f70,#5a5048)">
    <p class="abs card-eyebrow" style="left:16px;top:117px">CRAFTSMANSHIP</p>
    <p class="abs serif card-title" style="left:16px;top:131px">Where Tradition Meets Innovation</p>
    <div class="circle-arrow" style="left:234px;top:120px"><svg viewBox="0 0 9 6"><path d="M0 3h8M5.5 .5 8 3 5.5 5.5" stroke="#111" fill="none" stroke-width=".8"/></svg></div>
  </article>

  <article class="photo" role="img" aria-label="Worker in protective mask cutting metal with sparks" style="left:309px;top:1104px;width:265px;height:158px;background:linear-gradient(160deg,#cfcfcf,#6f7c8c)">
    <p class="abs card-eyebrow" style="left:16px;top:117px">BEHIND THE SCENES</p>
    <p class="abs serif card-title" style="left:16px;top:131px">Precision in Every Cut</p>
    <div class="circle-arrow" style="left:234px;top:120px"><svg viewBox="0 0 9 6"><path d="M0 3h8M5.5 .5 8 3 5.5 5.5" stroke="#111" fill="none" stroke-width=".8"/></svg></div>
  </article>

  <aside class="quote-box">
    <svg class="abs" style="left:241px;top:6px" width="24" height="15" viewBox="0 0 24 15"><path d="M5 0h6L6 15H0zM16 0h6l-5 15h-6z" fill="#fff"/></svg>
    <p class="abs small" style="left:16px;top:38px;width:250px">“True craftsmanship is measured not by what people see, but by the precision and care behind every detail. We build with integrity, so every project stands the test of time.”</p>
    <p class="abs" style="left:16px;top:82px;font-size:6px;font-weight:600">— Owen Hale, CEO</p>
  </aside>

  <article class="photo" role="img" aria-label="Retail boutique interior with arched wooden shelving and display table" style="left:309px;top:1395px;width:265px;height:158px;background:linear-gradient(180deg,#6a5a4a,#3a302a)">
    <p class="abs card-eyebrow" style="left:16px;top:117px">RETAIL INTERIORS</p>
    <p class="abs serif card-title" style="left:16px;top:131px">Bringing Retail Environments to Life</p>
    <div class="circle-arrow dark" style="left:234px;top:120px"><svg viewBox="0 0 9 6"><path d="M0 3h8M5.5 .5 8 3 5.5 5.5" stroke="#fff" fill="none" stroke-width=".8"/></svg></div>
  </article>

  <div class="rule-h" style="left:33px;top:1570px;width:541px"></div>
  <svg class="abs" style="left:33px;top:1630px" width="5" height="8" viewBox="0 0 5 8"><path d="M4 .5.8 4 4 7.5" stroke="#111" fill="none"/></svg>
  <p class="abs serif testimonial-name" style="left:80px;top:1605px">Clara Voss</p>
  <p class="abs" style="left:80px;top:1635px;font-size:5.5px;font-weight:600">Principal Architect, Voss Studio</p>
  <p class="abs small" style="left:261px;top:1604px;width:262px">“Halden Millwork consistently delivers exceptional craftsmanship with remarkable attention to detail. Their ability to translate complex architectural concepts into beautifully executed millwork makes them one of our most trusted partners.”</p>
  <svg class="abs" style="left:569px;top:1630px" width="5" height="8" viewBox="0 0 5 8"><path d="M1 .5 4.2 4 1 7.5" stroke="#111" fill="none"/></svg>
  <div class="rule-h" style="left:33px;top:1695px;width:541px"></div>

  <h2 class="abs serif" style="left:37px;top:1731px;font-size:22px;line-height:26px;color:var(--tan)">Let's Create Something<br>Exceptional.</h2>
  <div class="rule-v" style="left:435px;top:1727px;height:60px"></div>
  <div class="btn" style="left:471px;top:1748px;width:81px;height:18px">Let's Talk
    <svg viewBox="0 0 9 6"><path d="M0 3h8M5.5 .5 8 3 5.5 5.5" stroke="#fff" fill="none" stroke-width=".8"/></svg></div>

  <footer class="site-footer">
    <div class="foot-brand">Halden</div>
    <p class="abs tiny" style="left:127px;top:22px;width:170px">“Halden Millwork consistently delivers exceptional craftsmanship with remarkable attention to detail. Their ability to translate complex architectural concepts into beautifully executed millwork makes them one of our most trusted partners.”</p>
    <p class="abs tiny" style="left:127px;top:58px;color:#e1dcd4">Halden is a Minority Owned Business.<br>A Certified MBE.</p>
    <p class="abs serif" style="left:354px;top:22px;font-size:9px;color:#e1dcd4">Let's Talk</p>
    <p class="abs tiny" style="left:354px;top:40px">Halden Architectural Millwork<br>118 Larkin Row<br>Fairhaven, NC 27000</p>
    <svg class="abs" style="left:482px;top:27px" width="7" height="7" viewBox="0 0 7 7"><path d="M1.5 .5 3 2 2.2 3a4 4 0 0 0 1.8 1.8L5 4l1.5 1.5-1 1C2.5 6.5.5 4.5.5 1.5z" stroke="#cfcac2" fill="none" stroke-width=".6"/></svg>
    <p class="abs tiny" style="left:497px;top:26px">555.014.2290</p>
    <svg class="abs" style="left:482px;top:40px" width="8" height="6" viewBox="0 0 8 6"><rect x=".4" y=".4" width="7.2" height="5.2" stroke="#cfcac2" fill="none" stroke-width=".6"/><path d="M.4.4 4 3.4 7.6.4" stroke="#cfcac2" fill="none" stroke-width=".6"/></svg>
    <p class="abs tiny" style="left:497px;top:39px;text-decoration:underline">hello@haldenmillwork.com</p>
    <div class="social" style="left:482px;top:51px"></div>
    <div class="social" style="left:500px;top:51px"></div>
    <div class="rule-h" style="left:33px;top:90px;width:541px;background:#6d6a66"></div>
    <p class="abs tiny" style="left:45px;top:100px;word-spacing:16px">User&nbsp;Agreement Privacy&nbsp;Policy Careers Accessibility&nbsp;Help Site&nbsp;Map</p>
    <p class="abs tiny" style="left:454px;top:100px">All Rights Reserved. Halden Architectural Millwork</p>
  </footer>

</div>
</body>
</html>
```